Infographic Design for Company Explainer

We need an engaging infographic that concisely describes our neuroscience music composition process to potential new clients. The infographic should be clean, and not overly cluttered with imagery or text, and it should use our fonts and brand colours to express the basic message of how we conduct our work and the science involved in the process.

Please follow the attached INFOGRAPHIC GUIDELINE document, and we promise to seriously consider your design. You don't have to follow it 100%, but please use it as an inspiration for your work.

Target Market(s)

Professionals and Businesses

Font styles to use
Sans Serif
Other font styles liked:
• Raleway (headers and titles), Roboto (subtitles and text)

Colors

Designer to choose colors to be used in the design.

Requirements
Must have
• Design that is in line with the branding guide
Nice to have
• Visuals that are somewhat in line with our website tallowbright.com

```html
<!DOCTYPE html>
<html lang="en">
<head>
<meta charset="utf-8">
<title>Tallow Bright – Music Composition to Client Process</title>
<link href="https://fonts.googleapis.com/css2?family=Poppins:wght@500;600;700&family=Roboto:ital,wght@0,400;0,500;0,700;1,400&display=swap" rel="stylesheet">
<style>
:root{
  --backdrop:#8e8d97;
  --navy:#2b0d5c;
  --navy-deep:#24094f;
  --violet:#6b5cf0;
  --lavender:#8b80f7;
  --purple:#a040c8;
  --pink:#ee3d7c;
  --mint:#dff3f4;
  --lilac:#e3e1fb;
  --ink:#1e1140;
  --muted:#4b4666;
  --white:#ffffff;
}
*{box-sizing:border-box;margin:0;padding:0}
html,body{width:1200px;height:1200px;overflow:hidden}
body{background:var(--backdrop);font-family:"Roboto",sans-serif;color:var(--ink)}
.poster{position:absolute;left:190px;top:22px;width:820px;height:1156px;background:var(--white);overflow:hidden}
.header{height:94px;background:var(--navy);display:flex;align-items:center;padding:0 0 0 50px}
.brand{display:flex;align-items:center;gap:12px;color:var(--white);font-family:"Poppins",sans-serif;font-weight:500;font-size:27px;line-height:28px;width:208px}
.brand-dot{width:50px;height:50px;border-radius:50%;border:4px solid var(--pink);flex:none}
.process-pill{margin-left:auto;height:56px;width:553px;background:var(--lavender);border-radius:28px 0 0 28px;display:flex;align-items:center;padding-left:40px;color:var(--white);font-family:"Poppins",sans-serif;font-weight:600;font-size:25px}
.intro{height:209px;background:var(--mint);position:relative}
.intro-title{position:absolute;top:14px;width:100%;text-align:center;font-family:"Poppins",sans-serif;font-weight:600;font-size:27px;color:var(--navy)}
.intro-title span{color:var(--pink);letter-spacing:7px;margin-left:4px}
.clef-art{position:absolute;left:158px;top:68px;width:80px;height:116px;border-radius:40px;background:linear-gradient(160deg,#a040c8,#ee3d7c)}
.team-art{position:absolute;left:303px;top:64px;width:242px;height:110px;border-radius:10px 10px 0 0;background:linear-gradient(90deg,#ee3d7c,#3a2a86 45%,#6b5cf0 75%,#1ab8d0)}
.brain-badge{position:absolute;left:703px;top:58px;width:38px;height:38px;border-radius:50%;background:#f6dce8;border:2px solid var(--white)}
.intro-side{position:absolute;left:583px;top:84px;font-family:"Poppins",sans-serif;font-weight:600;font-size:21px;line-height:23px;color:var(--navy)}
.intro-side span{color:var(--violet)}
.intro-note{position:absolute;bottom:8px;width:100%;text-align:center;font-weight:500;font-size:16px;color:var(--navy)}
.results{height:422px;position:relative}
.results-title{position:absolute;top:10px;width:100%;text-align:center;font-family:"Poppins",sans-serif;font-weight:600;font-size:28px;color:var(--navy)}
.results-title span{color:var(--violet)}
.cycle{position:absolute;left:200px;top:21px}
.step{position:absolute;font-size:14.5px;line-height:17px;font-weight:500;color:var(--navy)}
.step b{font-family:"Poppins",sans-serif;font-size:21px;margin-right:3px}
.step-1{left:540px;top:58px;width:225px}.step-1 b{color:var(--pink)}
.step-2{left:592px;top:192px;width:205px}.step-2 b{color:var(--violet)}
.step-3{left:70px;top:300px;width:215px}.step-3 b{color:var(--navy)}
.step-4{left:40px;top:196px;width:185px}.step-4 b{color:var(--pink)}
.step small{display:block;font-style:italic;font-weight:400;font-size:10.5px;color:var(--muted);margin-top:6px}
.outcomes{height:380px;display:flex}
.benefits{width:416px;background:var(--lilac);padding-top:18px;position:relative}
.benefits h2{text-align:center;font-family:"Poppins",sans-serif;font-weight:500;font-size:18.5px;line-height:23px;color:var(--ink)}
.benefit{position:absolute;top:80px;width:190px}
.benefit-relax{left:18px}.benefit-focus{left:218px}
.benefit-photo{width:152px;height:152px;border-radius:50%;margin-left:18px;border:6px solid var(--violet)}
.benefit-relax .benefit-photo{background:radial-gradient(circle at 45% 55%,#e9e4e6,#cfc3c3)}
.benefit-focus .benefit-photo{border-color:var(--pink);background:radial-gradient(circle at 50% 50%,#c9d2d5,#8a9aa0)}
.benefit h3{margin-top:14px;font-family:"Poppins",sans-serif;font-weight:500;font-size:14.5px;color:var(--violet)}
.benefit-focus h3{color:var(--pink)}
.benefit .sub{font-size:12px;line-height:13px;font-weight:500;color:var(--ink)}
.benefit ul{list-style:none;margin-top:4px}
.benefit li{font-size:11.5px;line-height:13px;color:var(--muted);padding-left:9px;position:relative;margin-bottom:2px}
.benefit li::before{content:"";position:absolute;left:0;top:5px;width:4px;height:4px;border-radius:50%;background:var(--violet)}
.benefit-focus li::before{background:var(--pink)}
.academics{flex:1;background:var(--navy-deep);color:var(--white);padding:22px 26px 0 22px}
.academics h2{text-align:center;font-family:"Poppins",sans-serif;font-weight:600;font-size:18.5px;line-height:23px}
.academics h2 span{color:var(--lavender)}
.point{margin-top:20px;font-size:14px;line-height:16px;font-weight:500;padding-left:12px;position:relative}
.point::before{content:"";position:absolute;left:0;top:3px;border-left:6px solid var(--lavender);border-top:5px solid transparent;border-bottom:5px solid transparent}
.people{display:flex;justify-content:space-between;margin:18px 0 0 4px;width:340px}
.person{width:170px;text-align:center}
.person-photo{width:90px;height:90px;margin:0 auto;border-radius:50%;border:4px solid var(--white);box-shadow:0 0 0 2px var(--pink);background:linear-gradient(160deg,#e8e8e8,#9a9aa4)}
.person h4{margin-top:12px;font-family:"Poppins",sans-serif;font-weight:600;font-size:12.5px;color:var(--lavender)}
.person .role{font-style:italic;font-size:11.5px;color:var(--violet);line-height:13px}
.person .org{font-size:11.5px;line-height:13px}
.footer{height:51px;display:flex;align-items:center;justify-content:center;gap:8px;font-weight:500;font-size:15px;color:var(--ink)}
.email-pill{background:var(--pink);color:var(--white);border-radius:16px;padding:5px 16px;font-size:15.5px}
</style>
</head>
<body>
<main class="poster">
  <header class="header">
    <div class="brand"><span class="brand-dot"></span><span>tallow<br>bright</span></div>
    <div class="process-pill">Music Composition to Client PROCESS</div>
  </header>

  <section class="intro">
    <h1 class="intro-title">We engineer <span>MUSIC</span></h1>
    <div class="clef-art" role="img" aria-label="Illustration of a treble clef and music notes"></div>
    <div class="team-art" role="img" aria-label="Illustration of a group of composers standing together"></div>
    <div class="brain-badge" role="img" aria-label="Small brain icon"></div>
    <p class="intro-side">through<br><span>neuroscientific</span><br>principles.</p>
    <p class="intro-note">Our composers are versed in music cognition.</p>
  </section>

  <section class="results">
    <h2 class="results-title">We are driven by &nbsp;<span>Empirical Results</span>:</h2>
    <svg class="cycle" width="420" height="420" viewBox="0 0 420 420">
      <circle cx="210" cy="118" r="80" fill="#a040c8"/>
      <circle cx="302" cy="210" r="80" fill="#6b5cf0"/>
      <circle cx="210" cy="302" r="80" fill="#2b0d5c"/>
      <circle cx="118" cy="210" r="80" fill="#ee3d7c"/>
      <circle cx="210" cy="118" r="50" fill="#1a1a1a" stroke="#fff" stroke-width="4" role="img" aria-label="Image of a head filled with music notes"/>
      <circle cx="302" cy="210" r="50" fill="#9fb0be" stroke="#fff" stroke-width="4" role="img" aria-label="Photo of a person wearing an EEG headset"/>
      <circle cx="210" cy="302" r="50" fill="#7f9fb8" stroke="#fff" stroke-width="4" role="img" aria-label="Image of a crowd of small figures held in hands"/>
      <circle cx="118" cy="210" r="50" fill="#f3eef6" stroke="#fff" stroke-width="4" role="img" aria-label="Illustration of a colourful treble clef"/>
      <circle cx="210" cy="210" r="38" fill="#fff"/>
      <circle cx="210" cy="210" r="27" fill="none" stroke="#a040c8" stroke-width="5"/>
      <g stroke-width="3" fill="none">
        <path d="M95 85 L112 68 M102 68 L112 68 L112 78" stroke="#ee3d7c"/>
        <path d="M296 100 L312 116 M312 106 L312 116 L302 116" stroke="#a040c8"/>
        <path d="M330 318 L312 336 M312 326 L312 336 L322 336" stroke="#6b5cf0"/>
        <path d="M112 336 L95 320 M95 330 L95 320 L105 320" stroke="#2b0d5c"/>
      </g>
    </svg>
    <p class="step step-1"><b>1.</b>Create compositions to produce brainwave frequency profile changes</p>
    <p class="step step-2"><b>2.</b>Measuring brainwave changes using electrodes and EEG devices</p>
    <p class="step step-3"><b>3.</b>Conducting large-scale double blind behavioral experiments<small>(Further details provided in our research papers)</small></p>
    <p class="step step-4"><b>4.</b>Using experimental results to enhance our music compositions</p>
  </section>

  <section class="outcomes">
    <div class="benefits">
      <h2>Our music is designed to produce<br>brainwave patterns that are conducive to:</h2>
      <div class="benefit benefit-relax">
        <div class="benefit-photo" role="img" aria-label="Photo of a person sleeping peacefully"></div>
        <h3>RELAXATION &amp; DEEP SLEEP</h3>
        <p class="sub">(as in inducing lower brainwave frequencies)</p>
        <ul>
          <li>30-day study indicates DOUBLING of deep sleep</li>
          <li>Proven to reduce time needed to fall asleep and to decrease tossing and turning</li>
        </ul>
      </div>
      <div class="benefit benefit-focus">
        <div class="benefit-photo" role="img" aria-label="Photo of a focused person looking down"></div>
        <h3>FOCUS &amp; ENGAGEMENT</h3>
        <p class="sub">(as in inducing higher brainwave frequencies)</p>
        <ul>
          <li>Shown to increase focus by 40%</li>
          <li>Proven especially effective for helping with ADHD symptoms</li>
          <li>Shown to have additional benefits for introverted individuals</li>
        </ul>
      </div>
    </div>
    <div class="academics">
      <h2>TESTING &amp; EVOLVING OUR CRAFT<br>WITH <span>TOP ACADEMICS</span></h2>
      <p class="point">Engaging with renowned cognitive neuroscientists to conduct large-scale experiments</p>
      <div class="people">
        <div class="person">
          <div class="person-photo" role="img" aria-label="Portrait photo of the primary science advisor"></div>
          <h4>Dr. Lena Varga, PhD</h4>
          <p class="role">Primary Science Advisor</p>
          <p class="org">Cognitive Neuroscientist,<br>Northfield University</p>
        </div>
        <div class="person">
          <div class="person-photo" role="img" aria-label="Portrait photo of the director of science"></div>
          <h4>Dr. Owen Hartley, PhD</h4>
          <p class="role">Director of Science,</p>
          <p class="org">Tallow Bright</p>
        </div>
      </div>
      <p class="point">Pushing music cognition frontiers through engagements with academic institutions</p>
    </div>
  </section>

  <footer class="footer">
    <span>Check out research papers for more information, and reach out to us anytime at</span>
    <span class="email-pill">info@tallowbright.com</span>
  </footer>
</main>
</body>
</html>
```